Business card website / business card for website

We are a French website selling products Made in USA of quality, we need a business card to give from hand to hand and for deposit in the cartons of Each order. We-have the logo That I send in the attachments The theme is: US Vintage and find the compromised entre les national park ambience us and the atmosphere Brooklyn If you can make the feeling it's great The site www.latablederivebleue.com (opening April) You can change the logo a little gold in color it could ... we are a French website selling products Made in USA quality, we need a business card to give from hand to hand and deposit in cartons each order. we have the logo that I convey in the attached parts is the theme: Vintage embiance US and find a compromise between the atmosphere us national park and the atmosphere Brooklyn at: www.latablederivebleue.com (opening April) if you can the impression is great

Target Market(s)

25-50 YEARS man, woman.

Industry/Entity Type

Business

Contact Information for Business Card

www.latablederivebleue.com
N'oubliez pas que nous sommes là si vous avez besoin de nouscontact@latablederivebleue.com

Font styles to use
Serif

Requirements
Must have
• my logo with "general store", my email address preceded by the phrase: Do not forget that we are here if you need us My logo with the words "general store," my email address Preceded by the sentence: remember we're here if you need us (in french)
Nice to have
• i like this style: http://designcorbel.net/ideas/print-ideas/25-charming-old-style-business-card-designs/ must feel the Vintage America it must feel the Vintage America lice can change a little logo or to color ... You can change the logo a little gold in color it could ... i like kraft paper with red ....
Should not have

```html
<!DOCTYPE html>
<html lang="fr">
<head>
<meta charset="utf-8">
<title>La Table de Rive Bleue — Carte de visite</title>
<link href="https://fonts.googleapis.com/css2?family=Open+Sans:wght@400;600;700&display=swap" rel="stylesheet">
<style>
  :root {
    --backdrop: #2a2a2b;
    --kraft: #cbbd94;
    --kraft-deep: #b9a877;
    --ink: #1d1a17;
    --barn-red: #8e1f1b;
    --logo-tone: #a8794f;
  }
  * { box-sizing: border-box; margin: 0; padding: 0; }
  html, body {
    width: 1200px; height: 1000px; overflow: hidden;
    background: var(--backdrop);
    font-family: "Open Sans", Arial, sans-serif;
  }
  .sheet {
    position: relative; width: 1200px; height: 1000px;
  }
  .card {
    position: absolute; left: 280px; width: 640px; height: 366px;
    border-radius: 26px;
    background: radial-gradient(ellipse at 35% 30%, #d6c9a2 0%, var(--kraft) 55%, var(--kraft-deep) 100%);
    color: var(--ink);
  }
  .card--front { top: 84px; }
  .card--back  { top: 530px; }

  /* front */
  .brand-mark {
    position: absolute; left: 50%; top: 40px; transform: translateX(-50%);
    width: 190px; height: 190px; border-radius: 50%;
    background: radial-gradient(circle, #c7a57d 0%, var(--logo-tone) 100%);
  }
  .brand-name {
    position: absolute; left: 0; right: 0; top: 248px; text-align: center;
    font-size: 20px; font-weight: 600; letter-spacing: 2px; text-transform: uppercase;
  }
  .store-label {
    position: absolute; left: 0; right: 0; top: 290px; text-align: center;
    font-size: 22px; font-weight: 600; letter-spacing: 1.5px;
  }

  /* back */
  .identity { position: absolute; left: 52px; top: 56px; }
  .person-name { font-size: 34px; font-weight: 700; line-height: 1.1; }
  .person-name .surname { color: var(--barn-red); font-weight: 600; }
  .person-role { font-size: 22px; font-weight: 600; color: var(--barn-red); margin-top: 2px; }

  .contact { position: absolute; left: 52px; top: 170px; font-size: 16px; line-height: 1.55; }
  .contact dt { display: inline; color: var(--barn-red); font-weight: 700; margin-right: 8px; }
  .contact dd { display: inline; }
  .contact .line { display: block; }
  .reminder { margin: 14px 0 8px; font-size: 16px; line-height: 1.35; }
</style>
</head>
<body>
<main class="sheet">
  <section class="card card--front" aria-label="Recto">
    <div class="brand-mark" role="img" aria-label="Emblème du magasin : grange dessinée entourée d'un cachet circulaire"></div>
    <p class="brand-name">La Table de Rive Bleue</p>
    <p class="store-label">GÉNÉRAL STORE</p>
  </section>

  <section class="card card--back" aria-label="Verso">
    <div class="identity">
      <h1 class="person-name">ARMAND <span class="surname">DELACROIX</span></h1>
      <p class="person-role">FONDATEUR &amp; CEO</p>
    </div>
    <dl class="contact">
      <span class="line"><dt>Phone:</dt><dd>+000 987 654 321</dd></span>
      <span class="line"><dt>Web:</dt><dd>www.latablederivebleue.com</dd></span>
      <p class="reminder">N'oubliez pas que nous sommes<br>ici si vous avez besoin de nous</p>
      <span class="line"><dt>Email:</dt><dd>contact@latablederivebleue.com</dd></span>
    </dl>
  </section>
</main>
</body>
</html>
```